Ridgeway Sparks Business cards

We require somebody to design business cards for our new business.

Target Market(s)

Mining, haulage and civil.

Industry/Entity Type

Auto electrician in mining industry

Contact Information for Business Card

ABN, business email address, mobile number.

Colors
00AB8E
00BBA5
67D7C9
C6EFE9
E9F9F6

Requirements
Must have
• Services I offer: Breakdowns, Field Service, A/C Systems, Machine rewires, mine site vehicle fit outs

```html
<!DOCTYPE html>
<html lang="en">
<head>
<meta charset="utf-8">
<title>Ridgeway Sparks Business Cards</title>
<link href="https://fonts.googleapis.com/css2?family=Exo+2:wght@500;600;700;800&display=swap" rel="stylesheet">
<style>
  :root {
    --bg-top: #2a2a2a;
    --bg-bottom: #0e0e0e;
    --card: #121212;
    --teal: #4fc9bd;
    --teal-light: #a6e6de;
    --silver-dark: #9a9a9a;
    --silver-light: #e6e6e6;
    --white: #f2f2f2;
    --ink: #111111;
  }
  * { box-sizing: border-box; margin: 0; padding: 0; }
  html, body { width: 1200px; height: 875px; overflow: hidden; }
  body {
    position: relative;
    background: linear-gradient(160deg, var(--bg-top), var(--bg-bottom));
    font-family: "Exo 2", sans-serif;
    color: var(--white);
  }
  .card {
    position: absolute;
    width: 520px;
    height: 300px;
    background: var(--card);
    border-radius: 16px;
    overflow: hidden;
    box-shadow: 0 18px 40px rgba(0,0,0,.55);
  }
  .card--services { left: 50px; top: 140px; }
  .card--contact { left: 630px; top: 430px; }

  .brand {
    position: absolute;
    display: flex;
    align-items: center;
    gap: 10px;
  }
  .brand__mark {
    width: 16px; height: 16px;
    background: var(--teal);
  }
  .brand__name {
    font-weight: 800;
    font-size: 34px;
    letter-spacing: 1px;
    text-transform: uppercase;
    color: var(--teal);
  }
  .card--services .brand { left: 0; right: 0; top: 92px; justify-content: center; }
  .card--contact .brand { left: 28px; top: 118px; }
  .card--contact .brand__name { font-size: 28px; }

  .services {
    position: absolute;
    left: 0; right: 0; top: 190px;
    text-align: center;
    font-weight: 600;
    font-size: 15px;
    line-height: 1.7;
    color: var(--white);
  }
  .services .dot { color: var(--teal); margin: 0 6px; }

  .person {
    position: absolute;
    right: 40px; top: 26px;
    text-align: right;
  }
  .person__name { font-weight: 700; font-size: 28px; color: var(--teal); line-height: 1; }
  .person__role { font-weight: 600; font-size: 12px; color: var(--white); margin-top: 4px; }
  .tab {
    position: absolute;
    right: 0; top: 22px;
    width: 18px; height: 34px;
    background: var(--teal);
  }

  .band-silver {
    position: absolute;
    right: 0; top: 150px;
    width: 250px; height: 62px;
    background: linear-gradient(180deg, var(--silver-light), var(--silver-dark));
    clip-path: polygon(20px 0, 100% 0, 100% 100%, 0 100%);
  }
  .phone {
    position: absolute;
    right: 28px; top: 164px;
    display: flex; align-items: center; gap: 12px;
    font-weight: 700; font-size: 26px; color: var(--ink);
  }
  .phone svg { width: 22px; height: 22px; }
  .abn {
    position: absolute;
    right: 28px; top: 222px;
    font-weight: 700; font-size: 24px; color: var(--white);
  }
  .abn__label { color: var(--teal); margin-right: 6px; }

  .band-teal {
    position: absolute;
    left: 0; bottom: 0;
    width: 300px; height: 46px;
    background: linear-gradient(90deg, var(--teal-light), var(--teal));
    clip-path: polygon(0 0, 100% 0, calc(100% - 20px) 100%, 0 100%);
  }
  .email {
    position: absolute;
    left: 22px; bottom: 10px;
    font-weight: 700; font-size: 20px; color: var(--ink);
  }
</style>
</head>
<body>
  <section class="card card--services">
    <div class="brand">
      <span class="brand__mark"></span>
      <span class="brand__name">Ridgeway Sparks</span>
    </div>
    <p class="services">
      Breakdowns<span class="dot">•</span>Field Service<span class="dot">•</span>A/C Systems<span class="dot">•</span>Machine rewires<br>
      <span class="dot">•</span>Mine site vehicle fit outs
    </p>
  </section>

  <section class="card card--contact">
    <div class="tab"></div>
    <div class="person">
      <div class="person__name">Daniel Hart</div>
      <div class="person__role">Head contractor</div>
    </div>
    <div class="brand">
      <span class="brand__mark"></span>
      <span class="brand__name">Ridgeway Sparks</span>
    </div>
    <div class="band-silver"></div>
    <div class="phone">
      <svg viewBox="0 0 24 24" aria-hidden="true"><path fill="#111" d="M6.6 10.8a15.1 15.1 0 0 0 6.6 6.6l2.2-2.2a1 1 0 0 1 1-.25 11.4 11.4 0 0 0 3.6.57 1 1 0 0 1 1 1V20a1 1 0 0 1-1 1A17 17 0 0 1 3 4a1 1 0 0 1 1-1h3.5a1 1 0 0 1 1 1c0 1.25.2 2.45.57 3.57a1 1 0 0 1-.25 1z"/></svg>
      <span>555-014-2278</span>
    </div>
    <div class="abn"><span class="abn__label">ABN:</span>42 118 907 356</div>
    <div class="band-teal"></div>
    <div class="email">info@ridgewaysparks.com</div>
  </section>
</body>
</html>
```